Inkwork by Delma Web Design
@#26: I would like to see some type of tattoo gun icon as opposed to the curly whimsical things in the header. The blue is still a bit out of place. Maybe a bright read for the subscription highlight?
@All: The nav bar from #22 is what I am looking for! I love the little gun icon!
#28: Please use the Rose Tattoo font found in the feed back for the header...and is possible to use only the left gun and have them facing each other. Can also add a latest news section?
@#18: Like the textures. I would like the header with my name to be more prominent. Please review my feedback for previous entries to see ideas to where the creative process has taken us.
@#24/25: Please review feedback of other entries to see new color choices.
thanks,
@#16: The header is a bit too busy. The font would be better suited without all the extra photos behind it and I would like my name rather than the nav at the top. I really like the welcome and latest tattoo sections. I'm look for wine colors as opposed to the plum that coming across on my screen with these two entries.
@All: I've looked into using the Rose font from the owner and have paid his "donation" so please use http://www.glyphbarn.example/quill-ink.font?fpp=50&psize=l in the header. I'm also looking for individuals that can follow up after this design contest for coding work as well. Please send an email if this is something you are willing and able to do.
@#12: Looking really close here. I would like a more "tattooy" font used at the top. The multicolored curve and use of tattoo gun icon on buttons is what I am looking for. Color choice here is spot on.
@#13/14: Very nice header though I would like to see the colors reversed and the gradient a bit more prominent. The purple in both is a bit distracting. I actually like the curve of your #5 entry just wanted it to hang down as opposed to up but a single sweeping curve is also pleasing. The addition of the video section is spot on, though I like the smaller margin area of #13.
@#6: Love the soft glow of the headers text though I would like it to be a little more creative than just straight font. The Nav text is a little to rigid for my taste.
@#7: Very close with the header. I'd love to see it in a deep red as opposed to the purple. I understand what was on the brief sheet but my eyes have been opened and I like the look of red. I would like the nav bar to be a smoother integration (maybe same red?) as well and the use of the Tattoo gun icon is awesome!
@All: Please use the recently uploaded Merrick tattoo (boy in frame) for all future ideas...
@All: After looking over these for a few hours I'm really leaning towards the red in #3.
@All: Would like the nav "buttons" to have icons of some type (industry related would be nice...maybe some humor?!?!)
@#5:Closer with the curve but I would like it to be in the top "Inkwork by Delma" header and flow down from there if that is a good description.
@#3: Love the headings creativity and setup. I'm looking for the heading to curve into the main photo.
@gullbrook: I love the clean lines of these two. I would like the header to be a bit more creative/grandiose and to possibly curve over the main picture if the description makes sense and doable.
The integration of the owl as a tattoo is nice, but it is actually wall art so doesn't actually work in the scheme of things.
I will post more of my tattoo work to use in the layouts.
@other designers: MOAR ideas!

```html
<!DOCTYPE html>
<html lang="en">
<head>
<meta charset="utf-8">
<title>Inkwork by Delma</title>
<link rel="stylesheet" href="https://fonts.googleapis.com/css2?family=Jura:wght@400;600&family=Kaushan+Script&family=Great+Vibes&display=swap">
<style>
:root{
  --page:#262626;
  --page-edge:#141414;
  --wine:#6e0f16;
  --wine-dark:#2a0407;
  --wine-bright:#b3202b;
  --wine-line:#8a1a22;
  --hero:#0b0b0b;
  --ink:#ffffff;
  --muted:#cfcfcf;
  --band:#bdbdbd;
  --band-dark:#9a9a9a;
  --band-text:#3a3a3a;
  --heading-grey:#4a4a4a;
  --pill:#3b3b3b;
  --accent:#c9d23a;
  --icon:#d8d8d8;
}
*{margin:0;padding:0;box-sizing:border-box}
html,body{width:1200px;height:1072px;overflow:hidden}
body{background:radial-gradient(ellipse at 50% 40%,var(--page) 0%,var(--page-edge) 100%);font-family:"Jura",sans-serif;color:var(--ink);position:relative}
.site{position:absolute;left:72px;top:0;width:1058px;height:1000px;overflow:hidden}

.header{position:absolute;left:0;top:0;width:1058px;height:160px;background:linear-gradient(180deg,var(--wine-dark) 0%,var(--wine) 55%,#4a070d 100%);z-index:1}
.brand-mark{position:absolute;left:40px;top:42px;width:26px;height:26px;border-radius:50%;background:var(--ink)}
.brand{position:absolute;left:78px;top:30px;font-weight:600;font-size:42px;letter-spacing:1px}
.newsletter{position:absolute;left:740px;top:38px;width:290px;height:26px;background:#e9e9e9;color:#111;font-size:15px;font-weight:600;letter-spacing:1px;padding:4px 14px}
.newsletter::after{content:"";position:absolute;right:10px;top:7px;border-left:12px solid var(--wine-bright);border-top:6px solid transparent;border-bottom:6px solid transparent}
.nav{position:absolute;right:28px;top:112px;display:flex;gap:20px;list-style:none}
.nav li{font-family:"Great Vibes",cursive;font-size:27px;line-height:1}

.hero{position:absolute;left:0;top:160px;width:1058px;height:520px;background:linear-gradient(180deg,#1a1a1a 0%,var(--hero) 40%,#000 100%);overflow:hidden}
.tattoo{position:absolute;left:40px;top:10px;width:470px;height:510px;background:radial-gradient(ellipse at 50% 50%,#9c7a64 0%,#6b4f3f 55%,#2b211c 100%);border-radius:0 0 40px 0}
.greeting{position:absolute;left:530px;top:92px;font-size:64px;font-weight:400;letter-spacing:1px;line-height:1.1}
.intro{position:absolute;left:520px;top:178px;width:480px;font-size:24px;line-height:30px;text-align:right;color:var(--muted)}
.cta{position:absolute;left:740px;width:260px;font-size:18px;font-weight:600;text-align:right;padding-bottom:8px}
.cta span{color:var(--accent)}
.cta-work{top:300px;border-bottom:1px solid #555}
.cta-book{top:344px}

.swoosh{position:absolute;left:0;top:150px;z-index:1}

.features{position:absolute;left:0;top:680px;width:1058px;height:300px;background:linear-gradient(180deg,var(--band) 0%,#d2d2d2 50%,var(--band-dark) 100%)}
.dots{position:absolute;left:500px;top:694px;display:flex;gap:12px;z-index:2}
.dots i{width:11px;height:11px;border-radius:50%;background:#777;display:block}
.dots i:first-child{background:#eee}
.feature{position:absolute;top:48px;width:280px;color:var(--band-text)}
.feature h2{font-family:"Kaushan Script",cursive;font-weight:400;font-size:42px;line-height:1.2;color:var(--heading-grey)}
.feature .art{position:absolute;right:0;top:6px;width:66px;height:42px;border-radius:6px;background:linear-gradient(135deg,#8a8a8a,#5a5a5a)}
.feature p{font-size:12px;line-height:15px;margin-top:8px;height:90px}
.pill{display:block;margin:30px auto 0;width:190px;height:22px;border-radius:11px;background:var(--pill);color:#eee;font-size:12px;font-weight:600;text-align:center;line-height:22px}
.pill span{color:var(--accent)}
.f-artists{left:100px}.f-studio{left:395px}.f-location{left:695px}

.footer{position:absolute;left:0;top:1010px;width:1200px;height:40px}
.social{position:absolute;top:0;display:flex;align-items:center;gap:12px;font-size:17px;color:var(--muted)}
.social i{width:34px;height:34px;border-radius:50%;background:var(--icon);display:block}
.s-1{left:300px}.s-2{left:485px}.s-3{left:660px}.s-4{left:830px}
</style>
</head>
<body>
<div class="site">
  <header class="header">
    <span class="brand-mark"></span>
    <div class="brand">Inkwork by Delma</div>
    <div class="newsletter">GET THE NEWS LETTER</div>
    <ul class="nav">
      <li>Home</li><li>Services</li><li>Artists</li><li>Studio</li><li>Work</li><li>Contact</li>
    </ul>
  </header>
  <section class="hero">
    <div class="tattoo" role="img" aria-label="Photo of a framed portrait tattoo on a forearm"></div>
    <h1 class="greeting">Hey I'm Delma,</h1>
    <p class="intro">At my shop our team does tattoos of all shapes and sizes, come in and check out the shop.</p>
    <div class="cta cta-work">VIEW WORK <span>&gt;&gt;</span></div>
    <div class="cta cta-book">BOOK DELMA <span>&gt;&gt;</span></div>
  </section>
  <svg class="swoosh" width="1058" height="110" viewBox="0 0 1058 110">
    <path d="M0 10 L1058 10 L1058 36 C700 40 300 60 0 100 Z" fill="#4a070d"/>
    <path d="M0 100 C300 60 700 40 1058 36" fill="none" stroke="#8a1a22" stroke-width="3"/>
  </svg>
  <section class="features">
    <article class="feature f-artists">
      <h2>Artists</h2>
      <div class="art" role="img" aria-label="Small tattoo machine illustration"></div>
      <p>This is where a brief description of the artists would go. You would describe what they do and how they are related to you. But remember it is good for the text to be on the page.</p>
      <span class="pill">Meet Artists <span>&gt;&gt;</span></span>
    </article>
    <article class="feature f-studio">
      <h2>Studio</h2>
      <div class="art" role="img" aria-label="Small tattoo chair illustration"></div>
      <p>Here you would have a quick description of how you and your studio space came to be. You could talk about how the shop grew and show off some of the beautiful work made in it.</p>
      <span class="pill">View Studio <span>&gt;&gt;</span></span>
    </article>
    <article class="feature f-location">
      <h2>Location</h2>
      <div class="art" role="img" aria-label="Small vintage car illustration"></div>
      <p>Use this area to give a quick overview of where the shop is. You will tell people how close it sits to the town centre, share the street address and phone number, and note nearby parking.</p>
      <span class="pill">Check out Location <span>&gt;&gt;</span></span>
    </article>
  </section>
  <div class="dots"><i></i><i></i><i></i><i></i></div>
</div>
<footer class="footer">
  <div class="social s-1"><i></i>Chirper</div>
  <div class="social s-2"><i></i>Chirper</div>
  <div class="social s-3"><i></i>Scrapbook</div>
  <div class="social s-4"><i></i>Email</div>
</footer>
</body>
</html>
```